Integrated content management graphic

We are looking for a creative iteration for the attached file. We are currently in the process of renewing our branding and this graphic will be a center piece to our product marketing. Our website is www.brelvanto-docuhub.com for more information on products and company.
Future projects are available for designers submitting outstanding concepts and branding capability.

Target Market(s)

Audience is IT and anyone interested in integrating content management with their ERP/Accounting system.

Industry/Entity Type

Construction

Requirements
Must have
• The design must use the current color scheme associated with our website, yellow, black, grey. White can also be used. The design should be sleek.
Nice to have
• 3D Feel. The wheel could take on a stadium concept in 3d.

```html
<!DOCTYPE html>
<html lang="en">
<head>
<meta charset="utf-8">
<title>Brelvanto DocuHub – Integrated Content Management Wheel</title>
<link href="https://fonts.googleapis.com/css2?family=Quicksand:wght@300&family=Roboto+Condensed:wght@800&display=swap" rel="stylesheet">
<style>
  :root {
    --paper: #ffffff;
    --title-grey: #8c8c8c;
    --yellow: #f5cf00;
    --yellow-deep: #d4a400;
    --charcoal: #2c2c2c;
    --charcoal-deep: #161616;
    --steel: #a9a9a9;
    --steel-deep: #6b6b6b;
    --ink: #1b1b1b;
    --white: #ffffff;
  }
  html, body {
    margin: 0;
    padding: 0;
    width: 1200px;
    height: 524px;
    overflow: hidden;
    background: var(--paper);
  }
  .canvas {
    display: block;
    width: 1200px;
    height: 524px;
  }
  .variant-title {
    font-family: "Quicksand", sans-serif;
    font-weight: 300;
    font-size: 44px;
    fill: var(--title-grey);
    text-anchor: middle;
  }
  .label {
    font-family: "Roboto Condensed", sans-serif;
    font-weight: 800;
    text-anchor: middle;
    letter-spacing: 0.3px;
  }
  .label--outer { fill: var(--yellow); font-size: 13px; }
  .label--outer-large { fill: var(--yellow); font-size: 16px; }
  .label--outer-small { fill: var(--yellow); font-size: 11px; }
  .label--mid { fill: var(--ink); font-size: 12.5px; }
  .label--inner { fill: var(--white); font-size: 11.5px; }
  .label--inner-small { fill: var(--white); font-size: 9px; }
  .hub-name {
    font-family: "Roboto Condensed", sans-serif;
    font-weight: 800;
    font-size: 60px;
    fill: var(--yellow);
    text-anchor: middle;
    dominant-baseline: central;
  }
  .stop-yellow { stop-color: var(--yellow); }
  .stop-yellow-deep { stop-color: var(--yellow-deep); }
  .stop-charcoal { stop-color: var(--charcoal); }
  .stop-charcoal-deep { stop-color: var(--charcoal-deep); }
  .stop-steel { stop-color: var(--steel); }
  .stop-steel-deep { stop-color: var(--steel-deep); }
</style>
</head>
<body>
<svg class="canvas" viewBox="0 0 945 412" xmlns="http://www.w3.org/2000/svg" role="img" aria-label="Two variants of the integrated content management wheel">
  <defs>
    <linearGradient id="fill-outer" x1="0" y1="0" x2="0" y2="1">
      <stop offset="0" class="stop-charcoal"/>
      <stop offset="1" class="stop-charcoal-deep"/>
    </linearGradient>
    <linearGradient id="fill-mid" x1="0" y1="0" x2="0" y2="1">
      <stop offset="0" class="stop-yellow"/>
      <stop offset="1" class="stop-yellow-deep"/>
    </linearGradient>
    <linearGradient id="fill-inner" x1="0" y1="0" x2="0" y2="1">
      <stop offset="0" class="stop-steel"/>
      <stop offset="1" class="stop-steel-deep"/>
    </linearGradient>
    <radialGradient id="fill-hub" cx="0.5" cy="0.4" r="0.6">
      <stop offset="0" class="stop-charcoal"/>
      <stop offset="1" class="stop-charcoal-deep"/>
    </radialGradient>

    <!-- text guides: clockwise start at bottom, counter-clockwise start at top -->
    <path id="cw-171" d="M0,171 A171,171 0 1 1 0,-171 A171,171 0 1 1 0,171"/>
    <path id="cw-170" d="M0,170 A170,170 0 1 1 0,-170 A170,170 0 1 1 0,170"/>
    <path id="cw-122" d="M0,122 A122,122 0 1 1 0,-122 A122,122 0 1 1 0,122"/>
    <path id="cw-80" d="M0,80 A80,80 0 1 1 0,-80 A80,80 0 1 1 0,80"/>
    <path id="cw-88" d="M0,88 A88,88 0 1 1 0,-88 A88,88 0 1 1 0,88"/>
    <path id="cw-76" d="M0,76 A76,76 0 1 1 0,-76 A76,76 0 1 1 0,76"/>
    <path id="ccw-185" d="M0,-185 A185,185 0 1 0 0,185 A185,185 0 1 0 0,-185"/>
    <path id="ccw-141" d="M0,-141 A141,141 0 1 0 0,141 A141,141 0 1 0 0,-141"/>
    <path id="ccw-94" d="M0,-94 A94,94 0 1 0 0,94 A94,94 0 1 0 0,-94"/>

    <g id="ring-outer" fill="none" stroke-width="44">
      <circle r="177" pathLength="360" stroke-dasharray="28 332" stroke-dashoffset="-252"/>
      <circle r="177" pathLength="360" stroke-dasharray="38 322" stroke-dashoffset="-287"/>
      <circle r="177" pathLength="360" stroke-dasharray="90 270" stroke-dashoffset="-332"/>
      <circle r="177" pathLength="360" stroke-dasharray="42 318" stroke-dashoffset="-69"/>
      <circle r="177" pathLength="360" stroke-dasharray="57 303" stroke-dashoffset="-118"/>
      <circle r="177" pathLength="360" stroke-dasharray="63 297" stroke-dashoffset="-182"/>
    </g>
    <g id="ring-mid" fill="none" stroke-width="44">
      <circle r="130" pathLength="360" stroke-dasharray="100 260" stroke-dashoffset="-200"/>
      <circle r="130" pathLength="360" stroke-dasharray="36 324" stroke-dashoffset="-304"/>
      <circle r="130" pathLength="360" stroke-dasharray="130 230" stroke-dashoffset="-344"/>
      <circle r="130" pathLength="360" stroke-dasharray="78 282" stroke-dashoffset="-118"/>
    </g>
    <g id="ring-inner" fill="none" stroke-width="44">
      <circle r="82" pathLength="360" stroke-dasharray="86 274" stroke-dashoffset="-226"/>
      <circle r="82" pathLength="360" stroke-dasharray="84 276" stroke-dashoffset="-318"/>
      <circle r="82" pathLength="360" stroke-dasharray="86 274" stroke-dashoffset="-46"/>
      <circle r="82" pathLength="360" stroke-dasharray="84 276" stroke-dashoffset="-138"/>
    </g>

    <g id="wheel">
      <!-- depth layers -->
      <use href="#ring-outer" y="12" stroke="#0d0d0d"/>
      <use href="#ring-outer" stroke="url(#fill-outer)"/>
      <use href="#ring-mid" y="9" stroke="#9a7700"/>
      <use href="#ring-mid" stroke="url(#fill-mid)"/>
      <use href="#ring-inner" y="6" stroke="#4a4a4a"/>
      <use href="#ring-inner" stroke="url(#fill-inner)"/>
      <circle r="60" cy="4" fill="#0a0a0a"/>
      <circle r="58" fill="url(#fill-hub)" stroke="#555" stroke-width="2"/>

      <!-- outer ring: business systems -->
      <text class="label label--outer-small"><textPath href="#cw-171" startOffset="48.9%">ACCOUNTING</textPath></text>
      <text class="label label--outer"><textPath href="#cw-171" startOffset="60%">PROJECT MGMT</textPath></text>
      <text class="label label--outer-large"><textPath href="#cw-170" startOffset="79.7%">EQUIPMENT MGMT</textPath></text>
      <text class="label label--outer-large"><textPath href="#ccw-185" startOffset="50%">HR</textPath></text>
      <text class="label label--outer-large"><textPath href="#ccw-185" startOffset="34.4%">FACILITIES MGMT</textPath></text>
      <text class="label label--outer"><textPath href="#cw-171" startOffset="34.2%">PROPERTY MGMT</textPath></text>

      <!-- middle ring: platforms -->
      <text class="label label--mid"><textPath href="#cw-122" startOffset="44.4%">DESKSUITE</textPath></text>
      <text class="label label--mid"><textPath href="#cw-122" startOffset="64.4%">ERP</textPath></text>
      <text class="label label--mid"><textPath href="#ccw-141" startOffset="62.5%">PROJECT MGMT SOFTWARE</textPath></text>
      <text class="label label--mid"><textPath href="#ccw-141" startOffset="31.4%">TEAMVAULT</textPath></text>

      <!-- inner ring: core functions -->
      <text class="label label--inner"><textPath href="#cw-80" startOffset="50%">CAPTURE</textPath></text>
      <text class="label label--inner-small"><textPath href="#cw-88" startOffset="75%">DOCUMENT</textPath></text>
      <text class="label label--inner-small"><textPath href="#cw-76" startOffset="75%">MANAGEMENT</textPath></text>
      <text class="label label--inner"><textPath href="#ccw-94" startOffset="50%">WORKFLOW</textPath></text>
      <text class="label label--inner"><textPath href="#cw-80" startOffset="25%">ARCHIVING</textPath></text>

      <text class="hub-name" y="2">BD</text>
    </g>
  </defs>

  <text class="variant-title" x="225" y="36">Cm6a</text>
  <text class="variant-title" x="720" y="36">CM6b</text>

  <use href="#wheel" transform="translate(216,222) scale(1,0.9)"/>
  <use href="#wheel" transform="translate(714,222) scale(1,0.9)"/>
</svg>
</body>
</html>
```